Business Card for Technology Startup

Design a 2-sided business card using the logo provided. We are a digital healthcare platform that provides a mobile app and web UI that helps caregivers, families, and doctors share information and provide better patient outcomes. We use AI and machine learning to help guide patients through their day-to-day life. The final design should communicate stability, peace, comfort, but also align with the image of an AI-driven technology startup.

I'd like the deliverable to by a Photoshop PSD file (with layers) that I can work with in pixlr.com. Should contain the following editable layers:
Name (ex. John Doe)
Title (ex. Founder / CEO)
Email (ex. info@brenvaxa.ai)
Phone (ex. (555) 214-7086)
Website (ex. https://brenvaxa.ai)

```html
<!DOCTYPE html>
<html lang="en">
<head>
<meta charset="utf-8">
<title>Brenvaxa – Business Card</title>
<link rel="stylesheet" href="https://fonts.googleapis.com/css2?family=Poppins:wght@300;400;600&display=swap">
<style>
  :root {
    --backdrop: #969696;
    --card: #252525;
    --accent: #1ec1e8;
    --wordmark: #ffffff;
    --muted: #8c8c8c;
    --tagline: #6e6e6e;
    --divider: #3a4a50;
    --pattern-dark: #0c0c0c;
    --pattern-light: #2e2e2e;
  }
  * { margin: 0; padding: 0; box-sizing: border-box; }
  html, body {
    width: 1200px; height: 1000px; overflow: hidden;
    background: var(--backdrop);
    font-family: "Poppins", sans-serif;
  }
  .card {
    position: absolute; left: 253px; width: 693px; height: 399px;
    border-radius: 26px; background: var(--card); overflow: hidden;
  }
  .card--front { top: 71px; }
  .card--back { top: 515px; }

  .brand {
    position: absolute; left: 62px; top: 172px;
    display: flex; align-items: center; gap: 12px;
  }
  .brand__dot {
    width: 22px; height: 22px; border-radius: 50%; background: var(--accent);
  }
  .brand__name {
    font-weight: 600; font-size: 38px; line-height: 1; color: var(--wordmark);
    letter-spacing: 0.2px;
  }
  .divider {
    position: absolute; left: 348px; top: 117px; width: 1px; height: 165px;
    background: var(--divider);
  }
  .person { position: absolute; left: 385px; top: 126px; }
  .person__name {
    font-weight: 400; font-size: 28px; line-height: 1; color: var(--accent);
  }
  .person__title {
    margin-top: 4px; font-weight: 400; font-size: 14.5px; color: var(--muted);
    letter-spacing: 0.2px;
  }
  .contacts {
    position: absolute; left: 385px; top: 192px; list-style: none;
  }
  .contacts__item {
    display: flex; align-items: center; gap: 13px; height: 27.5px;
    font-weight: 300; font-size: 19.5px; color: var(--muted);
  }
  .contacts__icon { width: 16px; height: 16px; flex: none; }
  .tagline {
    position: absolute; left: 0; right: 0; top: 354px; text-align: center;
    font-weight: 400; font-size: 16px; letter-spacing: 3px; color: var(--tagline);
  }

  .back-pattern {
    position: absolute; inset: 0;
    background: linear-gradient(100deg, var(--pattern-dark) 0%, #1c1c1c 45%, var(--pattern-light) 100%);
  }
  .back-brand {
    position: absolute; left: 546px; top: 282px;
    font-weight: 600; font-size: 26px; line-height: 1; color: var(--accent);
    transform: translateX(-50%);
  }
</style>
</head>
<body>
  <section class="card card--front">
    <div class="brand">
      <span class="brand__dot"></span>
      <span class="brand__name">brenvaxa</span>
    </div>
    <div class="divider"></div>
    <div class="person">
      <h1 class="person__name">John Doe</h1>
      <p class="person__title">FOUNDER / CEO</p>
    </div>
    <ul class="contacts">
      <li class="contacts__item">
        <svg class="contacts__icon" viewBox="0 0 16 16" fill="none" stroke="var(--accent)" stroke-width="1.4">
          <rect x="1.5" y="3.5" width="13" height="9"/><path d="M1.5 3.5 8 9l6.5-5.5M1.5 12.5 6 7.5M14.5 12.5 10 7.5"/>
        </svg>
        <span>info@brenvaxa.ai</span>
      </li>
      <li class="contacts__item">
        <svg class="contacts__icon" viewBox="0 0 16 16" fill="none" stroke="var(--accent)" stroke-width="1.3">
          <path d="M4 1.5 6 4.5 4.8 6.2c.8 1.9 2.3 3.5 4.2 4.4L10.6 9.4l3 1.9-.9 2.6c-5.6-.3-10-4.9-10.2-10.4Z"/>
        </svg>
        <span>(555) 214-7086</span>
      </li>
      <li class="contacts__item">
        <svg class="contacts__icon" viewBox="0 0 16 16" fill="none" stroke="var(--accent)" stroke-width="1.1">
          <circle cx="8" cy="8" r="6.8"/><ellipse cx="8" cy="8" rx="3" ry="6.8"/><path d="M1.2 8h13.6M2.2 4.6h11.6M2.2 11.4h11.6M8 1.2v13.6"/>
        </svg>
        <span>brenvaxa.ai</span>
      </li>
    </ul>
    <p class="tagline">Bringing calm to every care moment.</p>
  </section>

  <section class="card card--back">
    <div class="back-pattern" role="img" aria-label="Repeating embossed brand pattern fading from black at left to charcoal at right"></div>
    <span class="back-brand">brenvaxa</span>
  </section>
</body>
</html>
```